Business Card Design for Event Planning Company

Create a business card for event planning company using our new logo. After I pick the design, I will need files made for 6 employees. Our company provides event design & logistics services as well as venue management. The font should be sans serif and complementary to the logo. I will need to know the name of the font selected for the final design. The phone numbers listed should be separated by "." not "-"

Address for the card
PO Box 318, Washington, DC 20019

Card One
Lorna Pettibone
lpettibone@galavoyant.com
202.481.7730

Card Two
Miriam Okonkwo
mokonkwo@galavoyant.com
202.556.2047

Card Three
Tessa Varnholt
tvarnholt@galavoyant.com
978.620.4471

Card Four
Robin Fess
rfess@galavoyant.com
202.718.3362

Card Five
Ada-Rose Pelletan-Uzor
adarose@galavoyant.com
202.839.1205

Card Six
Beatrix Holloway
Beatrix@galavoyant.com
202.492.6618

Target Market(s)

Corporate/Non-Profit

Industry/Entity Type

Event Planning

Contact Information for Business Card

Address for the card

Card One
Lorna Pettibone
lpettibone@galavoyant.com
202.481.7730

Card Two
Miriam Okonkwo
202.556.2047

Card Three
Tessa Varnholt
978.620.4471

Card Four
Robin Fess
rfess@galavoyant.com
202.718.3362

Card Five
Ada-Rose Pelletan-Uzor
202.839.1205

Card Six
Beatrix Holloway
202.492.6618

Font styles to use
Sans Serif

Colors

Designer to choose colors to be used in the design.

Requirements
Must have
• Two-sided with logo
Should not have
• Extra colors or be too busy

```html
<!DOCTYPE html>
<html lang="en">
<head>
<meta charset="utf-8">
<title>Galavoyant Business Card</title>
<link href="https://fonts.googleapis.com/css2?family=Open+Sans:wght@300;400;700&display=swap" rel="stylesheet">
<style>
  :root {
    --teal: #5aaeab;
    --ink: #231f20;
    --paper: #fafafa;
    --backdrop: #d4d4d4;
    --white: #ffffff;
  }
  * { margin: 0; padding: 0; box-sizing: border-box; }
  html, body {
    width: 1189px;
    height: 1200px;
    overflow: hidden;
    background: var(--backdrop);
    font-family: "Open Sans", Arial, sans-serif;
  }
  .card {
    position: absolute;
    left: 263px;
    width: 663px;
    height: 392px;
    background: var(--paper);
    overflow: hidden;
  }
  .card--front { top: 188px; }
  .card--back { top: 619px; }

  .wordmark {
    position: absolute;
    font-weight: 300;
    color: var(--teal);
    letter-spacing: 1px;
    white-space: nowrap;
    transform: translateX(-50%);
  }
  .card--front .wordmark {
    left: 178px;
    top: 152px;
    font-size: 42px;
  }
  .card--back .wordmark {
    left: 331px;
    top: 160px;
    font-size: 58px;
  }

  .divider {
    position: absolute;
    left: 359px;
    top: 53px;
    width: 2px;
    height: 220px;
    background: var(--ink);
  }
  .person {
    position: absolute;
    left: 390px;
    top: 70px;
  }
  .person__name {
    font-size: 28px;
    font-weight: 700;
    color: var(--ink);
    letter-spacing: -0.5px;
    line-height: 1.1;
  }
  .person__role {
    font-size: 16px;
    font-weight: 700;
    color: var(--teal);
    letter-spacing: 0.8px;
    line-height: 1.2;
  }
  .contact {
    position: absolute;
    left: 390px;
    top: 208px;
    list-style: none;
  }
  .contact__item {
    display: flex;
    align-items: center;
    gap: 10px;
    height: 27px;
    font-size: 15.5px;
    color: var(--ink);
  }
  .contact__icon {
    width: 16px;
    height: 16px;
    flex: none;
  }
  .accent-stripe {
    position: absolute;
    left: 0;
    top: 316px;
    width: 100%;
    height: 8px;
    background: var(--teal);
  }
  .address-band {
    position: absolute;
    left: 0;
    top: 326px;
    width: 100%;
    height: 66px;
    background: var(--ink);
    color: var(--white);
    font-size: 16px;
    display: flex;
    align-items: center;
    justify-content: center;
  }
</style>
</head>
<body>
  <section class="card card--front">
    <div class="wordmark">galavoyant</div>
    <div class="divider"></div>
    <div class="person">
      <div class="person__name">Lorna Pettibone</div>
      <div class="person__role">Your Position</div>
    </div>
    <ul class="contact">
      <li class="contact__item">
        <svg class="contact__icon" viewBox="0 0 16 16" aria-hidden="true">
          <rect width="16" height="16" fill="var(--teal)"/>
          <path d="M5 3 L7 5 L6 6.5 Q7 9 9.5 10 L11 9 L13 11 L11.5 13 Q6 12.5 3.5 5 Z" fill="var(--white)"/>
        </svg>
        <span>202.481.7730</span>
      </li>
      <li class="contact__item">
        <svg class="contact__icon" viewBox="0 0 16 16" aria-hidden="true">
          <rect width="16" height="16" fill="var(--teal)"/>
          <rect x="3" y="4.5" width="10" height="7" fill="none" stroke="var(--white)" stroke-width="1.2"/>
          <path d="M3 4.5 L8 8.5 L13 4.5" fill="none" stroke="var(--white)" stroke-width="1.2"/>
        </svg>
        <span>lpettibone@galavoyant.com</span>
      </li>
    </ul>
    <div class="accent-stripe"></div>
    <div class="address-band">PO Box 318, Washington, DC 20019</div>
  </section>

  <section class="card card--back">
    <div class="wordmark">galavoyant</div>
  </section>
</body>
</html>
```